Buisness card

**Front Side:**

**[Your Company Logo]**
**Steadfast Upkeep Industrial**
*Keeping Your Equipment Running Smoothly*

**Contact Information:**
- **Name:** [darren Whitlow
- **Title:** [owner
- **Phone:** [8025196047
- **Email:** darren@sukrn.com

**Back Side:**

**Services Offered:**
- Routine Inspections
- Equipment Maintenance
- Emergency Repairs
- Consultation Services
- New installs
Tag line
Be proactive not reactive

```html
<!DOCTYPE html>
<html lang="en">
<head>
<meta charset="utf-8">
<title>Steadfast Upkeep Industrial – Business Card</title>
<link rel="stylesheet" href="https://fonts.googleapis.com/css2?family=Open+Sans:wght@400;600;700;800&display=swap">
<style>
  :root {
    --navy: #062a78;
    --blue: #0a6ff2;
    --cyan: #00c8fb;
    --white: #ffffff;
    --ink: #444a55;
    --stage: #1c1c1f;
    --rule: #6b6f78;
  }
  * { box-sizing: border-box; margin: 0; padding: 0; }
  html, body {
    width: 1200px; height: 900px; overflow: hidden;
    background: var(--stage);
    font-family: "Open Sans", Arial, sans-serif;
  }
  .sheet {
    width: 1200px; height: 900px;
    display: flex; flex-direction: column; align-items: center; justify-content: center;
    gap: 40px;
  }
  .card {
    position: relative; width: 700px; height: 400px; overflow: hidden;
    box-shadow: 0 12px 30px rgba(0,0,0,.55);
  }

  /* Shared brand block */
  .brand-text { display: flex; flex-direction: column; }
  .brand-name {
    font-weight: 800; font-size: 19px; line-height: 1.15;
    color: var(--navy); text-transform: uppercase; max-width: 210px;
  }
  .brand-tagline {
    margin-top: 5px; font-weight: 700; font-size: 10.5px;
    letter-spacing: .04em; color: #1c1c22; text-transform: uppercase;
    white-space: nowrap;
  }

  /* Front */
  .card-front { background: var(--white); }
  .brand {
    position: absolute; left: 48px; top: 118px;
    display: flex; align-items: center; gap: 14px;
  }
  .brand-dot {
    width: 58px; height: 58px; border-radius: 50%;
    background: var(--navy); flex: none;
  }
  .divider {
    position: absolute; left: 362px; top: 100px;
    width: 1px; height: 142px; background: var(--rule);
  }
  .contact { position: absolute; left: 386px; top: 98px; }
  .contact-name {
    font-weight: 700; font-size: 34px; line-height: 1.1; color: var(--cyan);
  }
  .contact-title {
    font-size: 19px; color: var(--ink); margin-bottom: 12px;
  }
  .contact-line {
    display: flex; align-items: center; gap: 10px;
    font-size: 20px; color: var(--ink); line-height: 1.5;
  }
  .contact-line svg { width: 18px; height: 18px; flex: none; }
  .band {
    position: absolute; left: 0; right: 0; bottom: 0; height: 34px;
    display: flex; gap: 5px;
  }
  .band span { display: block; height: 100%; }
  .band-navy { width: 150px; background: var(--navy); }
  .band-blue { width: 270px; background: var(--blue); }
  .band-cyan { flex: 1; background: var(--cyan); }

  /* Back */
  .card-back { background: var(--navy); color: var(--white); }
  .back-brand { position: absolute; left: 40px; top: 34px; z-index: 1; }
  .back-brand .brand-name { color: var(--white); font-size: 22px; max-width: 300px; }
  .back-brand .brand-tagline { color: var(--white); font-size: 12px; }
  .services { position: absolute; left: 40px; top: 168px; z-index: 1; }
  .services-title {
    font-weight: 700; font-size: 22px; color: var(--cyan); margin-bottom: 6px;
  }
  .services-list { list-style: none; }
  .services-list li {
    font-size: 20px; line-height: 1.32; padding-left: 16px; position: relative;
  }
  .services-list li::before {
    content: ""; position: absolute; left: 0; top: 12px;
    width: 7px; height: 7px; border-radius: 50%; background: var(--cyan);
  }
  .dial-area {
    position: absolute; right: -150px; top: 10px;
    width: 500px; height: 500px; border-radius: 50%; background: var(--white);
  }
</style>
</head>
<body>
<main class="sheet">

  <section class="card card-front" aria-label="Business card front">
    <div class="brand">
      <div class="brand-dot"></div>
      <div class="brand-text">
        <span class="brand-name">Steadfast Upkeep Industrial</span>
        <span class="brand-tagline">Be proactive not reactive</span>
      </div>
    </div>
    <div class="divider"></div>
    <div class="contact">
      <p class="contact-name">darren Whitlow</p>
      <p class="contact-title">owner</p>
      <p class="contact-line">
        <svg viewBox="0 0 24 24" aria-hidden="true"><path fill="#00c8fb" d="M6.6 10.8a15.1 15.1 0 0 0 6.6 6.6l2.2-2.2a1 1 0 0 1 1-.25 11.4 11.4 0 0 0 3.6.57 1 1 0 0 1 1 1V20a1 1 0 0 1-1 1A17 17 0 0 1 3 4a1 1 0 0 1 1-1h3.5a1 1 0 0 1 1 1c0 1.25.2 2.45.57 3.6a1 1 0 0 1-.25 1z"/></svg>
        8025196047
      </p>
      <p class="contact-line">
        <svg viewBox="0 0 24 24" aria-hidden="true"><path fill="#00c8fb" d="M2 6h20v12H2z"/><path fill="none" stroke="#fff" stroke-width="1.8" d="M2 6l10 7 10-7"/></svg>
        darren@sukrn.com
      </p>
    </div>
    <div class="band">
      <span class="band-navy"></span>
      <span class="band-blue"></span>
      <span class="band-cyan"></span>
    </div>
  </section>

  <section class="card card-back" aria-label="Business card back">
    <div class="dial-area" role="img" aria-label="Large company emblem with gauge dial"></div>
    <div class="back-brand brand-text">
      <span class="brand-name">Steadfast Upkeep Industrial</span>
      <span class="brand-tagline">Be proactive not reactive</span>
    </div>
    <div class="services">
      <h2 class="services-title">Services Offered:</h2>
      <ul class="services-list">
        <li>Routine Inspections</li>
        <li>Equipment Maintenance</li>
        <li>Emergency Repairs</li>
        <li>Consultation Services</li>
        <li>New installs</li>
      </ul>
    </div>
  </section>

</main>
</body>
</html>
```